Letterhead to Prospective Clients

Create a letterhead (word & canva) that I will use to send letters to prospective clients and also include the Coralwood Estate Partners Logo, My Contact Details and Interchangeable "Suburb". Use the same font and colour pallete

Maris Dulworth | "Suburb" Specialist - Coral Shores & Surrounds
Mobile: 0417 862 095
Email: MD@CoralwoodEstatePartners.com.au

```html
<!DOCTYPE html>
<html lang="en">
<head>
<meta charset="utf-8">
<title>Coralwood Estate Partners – Letterhead</title>
<link href="https://fonts.googleapis.com/css2?family=Montserrat:wght@400;500&family=Source+Sans+3:wght@400&display=swap" rel="stylesheet">
<style>
  :root {
    --backdrop: #e6e6e6;
    --paper: #ffffff;
    --navy: #131a33;
    --tan: #d3a473;
    --body-grey: #545454;
    --ink: #1d1d1d;
  }
  * { margin: 0; padding: 0; box-sizing: border-box; }
  html, body {
    width: 1200px; height: 1079px; overflow: hidden;
    background: var(--backdrop);
  }
  .letterhead {
    position: absolute; left: 232px; top: 20px;
    width: 735px; height: 1040px;
    background: var(--paper);
    box-shadow: 0 6px 18px rgba(0,0,0,0.18);
    font-family: "Montserrat", sans-serif;
    color: var(--ink);
  }
  .brand {
    position: absolute; left: 70px; top: 82px;
    font-family: "Montserrat", sans-serif;
    font-weight: 400; font-size: 27px; letter-spacing: 0.12em;
    color: var(--navy); text-transform: uppercase;
    display: flex; align-items: center; gap: 12px;
  }
  .brand-dot { width: 10px; height: 10px; border-radius: 50%; background: var(--tan); }
  .sender { position: absolute; left: 70px; top: 265px; }
  .sender-name { font-size: 19px; font-weight: 400; color: var(--ink); }
  .sender-role { font-size: 13px; line-height: 18px; margin-top: 2px; }
  .letter-body {
    position: absolute; left: 70px; top: 353px; width: 595px;
    font-family: "Source Sans 3", sans-serif;
    font-size: 10.6px; line-height: 18px; color: var(--body-grey);
    text-align: justify;
  }
  .letter-body p + p { margin-top: 15px; }
  .sign-off {
    position: absolute; left: 70px; top: 705px;
    font-family: "Source Sans 3", sans-serif; color: var(--body-grey);
  }
  .sign-off .closing { font-size: 12px; }
  .signature-mark {
    width: 92px; height: 26px; margin-top: 14px;
    background: linear-gradient(90deg, #e7e9ee, #f3f4f7);
    border-radius: 3px;
  }
  .sign-off .signer { font-size: 14px; margin-top: 6px; }
  .footer {
    position: absolute; left: 70px; right: 70px; top: 900px;
    font-size: 12.5px; line-height: 18.5px; color: var(--ink);
  }
  .footer-address { position: absolute; left: 0; top: 25px; font-style: normal; }
  .footer-abn { position: absolute; left: 182px; top: 34px; }
  .footer-abn .label { color: var(--tan); }
  .footer-contact { position: absolute; right: 0; top: 0; list-style: none; }
  .footer-contact li { display: flex; align-items: center; gap: 5px; }
  .footer-contact svg { width: 10px; height: 10px; flex: none; }
  .accent-band {
    position: absolute; left: 0; bottom: 0; width: 100%; height: 16px;
    background: var(--tan);
  }
</style>
</head>
<body>
<main class="letterhead">
  <header class="brand"><span>Coralwood Estate Partners</span><span class="brand-dot"></span></header>

  <section class="sender">
    <h1 class="sender-name">Maris Dulworth</h1>
    <p class="sender-role">"Suburb" Specialist -<br>Coral Shores &amp; Surrounds</p>
  </section>

  <section class="letter-body">
    <p>Proin gravida nibh vel velit auctor aliquet. Aenean sollicitudin, lorem quis bibendum auctor, nisi elit consequat ipsum, nec sagittis sem nibh id elit. Duis sed odio sit amet nibh vulputate cursus a sit amet mauris. Morbi accumsan ipsum velit. Nam nec tellus a odio tincidunt auctor a ornare odio. Sed non mauris vitae erat consequat auctor eu in elit. Class aptent taciti sociosqu ad litora torquent ugue. Sed non neque elit. Sed ut imperdiet nisi. Proin condimentum fermentum nunc. Etiam pharetra, imperdiet nisi. Proin condimentum fermentum nunc. Etiam pharetra, erat sed fermentum feugiat, velit mauris egestas quam, ut aliquam massa nisl quis neque. Suspendisse in orci enim.</p>
    <p>Vivamus porta luctus erat id tempus. Proin gravida nibh vel velit auctor aliquet. Aenean sollicitudin, lorem quis bibendum auctor, nisi elit consequat ipsum, nec sagittis sem nibh id elit. Duis sed odio sit amet nibh vulputate cursus a sit amet mauris. Mo rbi accumsan ipsum velit. Nam nec tellus a odio tincidunt auctor a ornare odio. Sed non mauris vitae erat consequat auctor eu in elit. Class aptt consequat auctor eu in elit. Class aptent taciti sociosqu ad litora torquent per conubia nostra, per inceptos himenaeos. Mauris in erat justo.</p>
    <p>Nullam ac urna eu felis dapibus condimentum sit amet a augue. Sed non neque elit. Sed ut imperdiet nisi. Proin condimentum fermentum nunc. Etiam pharetra, erat sed fermentum feugiat, velit mauris egestas quam.Nullam ac urna eu felis dapibus condimentum sit amet a aug pharetra, erat sed fermentum feugiat, velit mauris egestas quam.Nullam ac urna eu felis dapibus condimentum sit amet a augue. Sed non neque elit. Sed ut imperdiet nisi. Proin condimentum fermentum nunc.</p>
  </section>

  <section class="sign-off">
    <p class="closing">Sincerely,</p>
    <div class="signature-mark" role="img" aria-label="Handwritten signature"></div>
    <p class="signer">Maris Dulworth</p>
  </section>

  <footer class="footer">
    <address class="footer-address">Shop 4/58 Tidewater<br>Road, Marlow QLD 4172</address>
    <p class="footer-abn"><span class="label">ABN:</span> 47 218 503 961</p>
    <ul class="footer-contact">
      <li>
        <svg viewBox="0 0 10 10" aria-hidden="true"><rect x="2.5" y="0.5" width="5" height="9" rx="1" fill="none" stroke="var(--tan)" stroke-width="1"/><line x1="4.3" y1="8" x2="5.7" y2="8" stroke="var(--tan)" stroke-width="0.8"/></svg>
        0417 862 095
      </li>
      <li>
        <svg viewBox="0 0 10 10" aria-hidden="true"><rect x="0.5" y="2" width="9" height="6" fill="var(--tan)"/><polyline points="0.5,2 5,5.5 9.5,2" fill="none" stroke="#fff" stroke-width="0.8"/></svg>
        MD@CoralwoodEstatePartners.com.au
      </li>
      <li>
        <svg viewBox="0 0 10 10" aria-hidden="true"><circle cx="5" cy="5" r="4.3" fill="none" stroke="var(--tan)" stroke-width="1"/><ellipse cx="5" cy="5" rx="1.8" ry="4.3" fill="none" stroke="var(--tan)" stroke-width="0.7"/><line x1="0.7" y1="5" x2="9.3" y2="5" stroke="var(--tan)" stroke-width="0.7"/></svg>
        www.coralwoodestatepartners.com.au
      </li>
    </ul>
  </footer>

  <div class="accent-band"></div>
</main>
</body>
</html>
```